Sales Training Power Point Presentation

We are looking for a power point presentation that allows us to turn our training manual into a presentation. I am attaching the training manual here, just to give an idea of what we will be presenting. We want to be able to have graphs for some of that data and be able to move around slides/edit as we see it is needed.

Target Market(s)

new sales employees

Industry/Entity Type

staffing

Colors
0054AA
0677BA
7BADD7
CADEEF
E8F1F8
F0912C
F2A743
F7CA91
FBE8D2
FDF5EE

Requirements
Must have
• graphs

```html
<!DOCTYPE html>
<html lang="en">
<head>
<meta charset="utf-8">
<title>Vantora Group — Sales Training Deck</title>
<link rel="stylesheet" href="https://fonts.googleapis.com/css2?family=Montserrat:wght@400;500;600;700;800;900&display=swap">
<style>
:root{
  --canvas:#cfd0e6;
  --navy:#2b3446;
  --navy-deep:#1f2636;
  --orange:#f07a2c;
  --orange-soft:#f5a06a;
  --paper:#ffffff;
  --ink:#3a3f4a;
  --muted:#7b808c;
  --rule:#d9dbe3;
  --highlight:#f6f2a8;
}
*{box-sizing:border-box;margin:0;padding:0}
html,body{width:863px;height:1200px;overflow:hidden}
body{background:var(--canvas);font-family:"Montserrat",Arial,sans-serif;color:var(--ink);position:relative}
.slide{position:absolute;width:262px;height:171px;background:var(--paper);overflow:hidden;box-shadow:0 6px 8px -4px rgba(40,40,80,.35)}
.col-1{left:20px}.col-2{left:300px}.col-3{left:580px}
.row-1{top:190px}.row-2{top:401px}.row-3{top:612px}.row-4{top:823px}

.slide-title{position:absolute;left:10px;top:9px;font-size:7.4px;line-height:8.4px;text-transform:uppercase;font-weight:500}
.slide-title .kicker{color:var(--orange);display:block}
.slide-title .heading{color:var(--navy);font-weight:600;display:block}
.brand{position:absolute;right:9px;top:8px;display:flex;flex-direction:column;align-items:center;gap:1px}
.brand .dot{width:6px;height:6px;border-radius:50%;background:var(--orange)}
.brand .name{font-size:3.4px;font-weight:700;color:var(--navy);letter-spacing:.2px}
.footer{position:absolute;left:0;right:0;bottom:9px;height:6px}
.footer .bar{position:absolute;left:0;top:2px;width:218px;height:2.4px;background:var(--orange);border-radius:0 2px 2px 0}
.footer .label{position:absolute;right:8px;top:0;font-size:3.2px;color:var(--navy);font-weight:500;display:flex;gap:2px;align-items:center}
.footer .label i{display:inline-block;width:.5px;height:6px;background:var(--orange)}
.slide.dark .footer .label{color:#fff}

.body{position:absolute;left:10px;right:10px;top:32px;font-size:2.7px;line-height:3.3px;color:var(--ink)}
.body p{margin-bottom:2.6px;text-align:justify}
.body .accent{color:var(--orange);font-weight:600}
.body ul{list-style:none;margin-bottom:2.6px}

/* photo slides */
.photo{position:absolute;inset:0;background:linear-gradient(120deg,#3c4558 0%,#232a3a 55%,#2e3647 100%)}
.photo::after{content:"";position:absolute;inset:0;background:rgba(31,38,54,.55)}
.hero-tab{position:absolute;left:0;top:0;background:var(--paper);display:flex;align-items:center;justify-content:center;flex-direction:column;gap:3px}
.hero-tab .dot{width:11px;height:11px;border-radius:50%;background:var(--orange)}
.hero-tab .name{font-size:7px;font-weight:700;color:var(--navy);letter-spacing:.8px}
.hero-title{position:absolute;color:#fff;font-weight:400;text-transform:uppercase;letter-spacing:.2px}
.hero-title em{font-style:normal;color:var(--orange);font-weight:600}
.hero-sub{color:var(--orange);font-size:3.6px;margin-top:2px;text-transform:none;letter-spacing:0}
.hero-copy{position:absolute;color:#fff;font-size:2.5px;line-height:3.3px}
.date-pill{position:absolute;background:var(--orange);color:#fff;font-size:3px;padding:1.5px 5px;border-radius:3px}
.url{position:absolute;color:#fff;font-size:3.2px}
.thanks{position:absolute;color:#fff;font-weight:900;font-size:27px;letter-spacing:.5px}
.thanks em{font-style:normal;color:var(--orange)}

/* tables */
.grid-table{border-collapse:collapse;width:100%;font-size:3px;text-align:center}
.grid-table th{color:#fff;font-weight:500;padding:1.4px 0}
.grid-table td{padding:1.5px 0;border:.4px solid var(--rule);background:#fff;color:var(--navy);font-weight:500}
.grid-table.orange-head th{background:var(--orange)}
.grid-table.navy-head th{background:var(--navy)}

.stat-table{border-collapse:collapse;font-size:2.1px;line-height:2.7px;color:var(--ink);width:100%}
.stat-table th{font-weight:700;text-align:left}
.stat-table td.hl{background:var(--highlight)}
.pie-card{position:absolute;border:.5px solid #555;background:#fff;display:flex;flex-direction:column;align-items:center;padding-top:2px}
.pie-card .cap{font-size:2.2px;font-weight:700;text-align:center;line-height:2.6px}
</style>
</head>
<body>

<!-- Row 1 -->
<section class="slide dark col-1 row-1" aria-label="Cover slide">
  <div class="photo" role="img" aria-label="Photo of a business team meeting in an office"></div>
  <div class="hero-tab" style="width:104px;height:36px;"><span class="dot"></span><span class="name">VANTORA GROUP</span></div>
  <h1 class="hero-title" style="left:17px;top:74px;font-size:9.6px;line-height:11px;">Powering <em>Progression</em><br>With People
    <span class="hero-sub" style="display:block">Recruitment solutions for an evolving marketplace.</span></h1>
  <p class="hero-copy" style="left:17px;top:109px;width:120px;">Lorem ipsum dolor sit amet, consectetuer adipiscing elit, sed diam nonummy nibh euismod tincidunt ut laoreet dolore magna aliquam erat volutpat.</p>
  <span class="date-pill" style="left:17px;top:126px;">28 July 2023</span>
  <span class="url" style="left:17px;top:155px;">www.vantoragroup.com</span>
</section>

<section class="slide col-2 row-1" aria-label="Sales training introduction">
  <h2 class="slide-title"><span class="kicker">Sales Training</span><span class="heading">Introduction</span></h2>
  <div class="brand"><span class="dot"></span><span class="name">VANTORA GROUP</span></div>
  <div class="body">
    <p>Welcome to our sales training guide. We are excited that you have joined the team, and our goal is to arm you for success in a worthwhile career.</p>
    <p>The following pages outline industry acumen, our value proposition, the sales cycle, daily activity and the building of an individual business plan.</p>
    <p>Selling means exchanging a service for money. There are many techniques and tools, yet all share one end goal: creating lasting value for clients.</p>
    <p>As you study these processes you will see that excelling in sales is more complex than a definition implies.</p>
    <p>The business world keeps evolving. A well trained professional sees change as opportunity and uses skills, product knowledge and focus to capitalize on it.</p>
    <p>Certain principles prove successful regardless of background. Throughout this course we will work toward mastery of the techniques that yield results.</p>
  </div>
  <div class="footer"><span class="bar"></span><span class="label">VANTORA GROUP <i></i> 01</span></div>
</section>

<section class="slide col-3 row-1" aria-label="Sales training introduction continued">
  <h2 class="slide-title"><span class="kicker">Sales Training</span><span class="heading">Introduction</span></h2>
  <div class="brand"><span class="dot"></span><span class="name">VANTORA GROUP</span></div>
  <div class="body">
    <p>Growing reliance on computers and technology has changed sales forever. Information is easier to find, and staying ahead means using modern tools well.</p>
    <p>We will also help you map a business plan, beginning with an honest self appraisal and ending with a clear, achievable goal for your first year.</p>
    <p>Sales is a rewarding career. The environment changes often, bringing difficult yet satisfying challenges. Be prepared with a full understanding of what we sell.</p>
  </div>
  <div class="footer"><span class="bar"></span><span class="label">VANTORA GROUP <i></i> 01</span></div>
</section>

<!-- Row 2 -->
<section class="slide col-1 row-2" aria-label="Industry acumen">
  <h2 class="slide-title"><span class="kicker">Industry</span><span class="heading">Acumen</span></h2>
  <div class="brand"><span class="dot"></span><span class="name">VANTORA GROUP</span></div>
  <div class="body">
    <p>For over a century the staffing industry has helped employers locate employees. As the market has grown, firms now serve nearly every sector.</p>
    <p class="accent">The staffing industry is made up of these types of firms:</p>
    <ul><li>· Contract Services Firm</li><li>· Direct Placement Firms</li><li>· Blended Services</li><li>· Executive Search Firms</li></ul>
    <p>These organizations may be generalists or specialize in niches such as office, industrial, technical, medical and home care.</p>
    <p>The first employment agencies in the country opened in the late 1800s.</p>
    <p>Years ago placement fees were paid by the candidate. Today client companies pay most agency fees.</p>
    <p>The temporary help industry has the majority of customers.</p>
    <p>In 2018, revenues in staffing were $167 billion.</p>
    <p>According to the National Staffing Council, most companies use temporary help.</p>
  </div>
  <div class="footer"><span class="bar"></span><span class="label">VANTORA GROUP <i></i> 01</span></div>
</section>

<section class="slide col-2 row-2" aria-label="Industry acumen chart">
  <h2 class="slide-title"><span class="kicker">Industry</span><span class="heading">Acumen</span></h2>
  <div class="brand"><span class="dot"></span><span class="name">VANTORA GROUP</span></div>
  <p style="position:absolute;left:10px;top:34px;font-size:3.8px;font-weight:700;color:var(--navy)">Staffing and Recruiting Industry Sales Increased 3.9% to $167 Billion in 2018</p>
  <svg style="position:absolute;left:8px;top:42px" width="240" height="106" viewBox="0 0 240 106" aria-label="Bar chart of annual staffing sales 2003 to 2018">
    <text x="10" y="4" font-size="2.4" fill="#333" font-weight="600">Sales (Billions of U.S. Dollars) — Annual Totals for Staffing and Recruiting Industry</text>
    <rect x="16" y="8" width="3" height="2" fill="#f07a2c"/><text x="20" y="9.8" font-size="2.2" fill="#333">Search and Placement</text>
    <rect x="16" y="11.5" width="3" height="2" fill="#2e4a7a"/><text x="20" y="13.3" font-size="2.2" fill="#333">Temporary and Contract</text>
    <g stroke="#e3e3e3" stroke-width=".3">
      <line x1="12" y1="95" x2="236" y2="95"/><line x1="12" y1="80" x2="236" y2="80"/><line x1="12" y1="65" x2="236" y2="65"/><line x1="12" y1="50" x2="236" y2="50"/><line x1="12" y1="35" x2="236" y2="35"/><line x1="12" y1="20" x2="236" y2="20"/>
    </g>
    <g font-size="2.2" fill="#555">
      <text x="2" y="96">$0</text><text x="1" y="81">$40</text><text x="1" y="66">$80</text><text x="0" y="51">$120</text><text x="0" y="36">$160</text>
    </g>
    <g fill="#2e4a7a">
      <rect x="16" y="70" width="9" height="25"/><rect x="30" y="66" width="9" height="29"/><rect x="44" y="62" width="9" height="33"/><rect x="58" y="59" width="9" height="36"/>
      <rect x="72" y="58" width="9" height="37"/><rect x="86" y="60" width="9" height="35"/><rect x="100" y="69" width="9" height="26"/><rect x="114" y="62" width="9" height="33"/>
      <rect x="128" y="56" width="9" height="39"/><rect x="142" y="54" width="9" height="41"/><rect x="156" y="50" width="9" height="45"/><rect x="170" y="48" width="9" height="47"/>
      <rect x="184" y="46" width="9" height="49"/><rect x="198" y="44" width="9" height="51"/><rect x="212" y="42" width="9" height="53"/><rect x="226" y="40" width="9" height="55"/>
    </g>
    <g fill="#f07a2c">
      <rect x="16" y="65" width="9" height="5"/><rect x="30" y="60" width="9" height="6"/><rect x="44" y="56" width="9" height="6"/><rect x="58" y="52" width="9" height="7"/>
      <rect x="72" y="51" width="9" height="7"/><rect x="86" y="53" width="9" height="7"/><rect x="100" y="63" width="9" height="6"/><rect x="114" y="56" width="9" height="6"/>
      <rect x="128" y="49" width="9" height="7"/><rect x="142" y="46" width="9" height="8"/><rect x="156" y="41" width="9" height="9"/><rect x="170" y="38" width="9" height="10"/>
      <rect x="184" y="36" width="9" height="10"/><rect x="198" y="33" width="9" height="11"/><rect x="212" y="31" width="9" height="11"/><rect x="226" y="28" width="9" height="12"/>
    </g>
    <g font-size="2.2" fill="#222" font-weight="700" text-anchor="middle">
      <text x="20.5" y="63.5">$80</text><text x="34.5" y="58.5">$92</text><text x="48.5" y="54.5">$104</text><text x="62.5" y="50.5">$113</text>
      <text x="76.5" y="49.5">$116</text><text x="90.5" y="51.5">$112</text><text x="104.5" y="61.5">$85</text><text x="118.5" y="54.5">$108</text>
      <text x="132.5" y="47.5">$124</text><text x="146.5" y="44.5">$129</text><text x="160.5" y="39.5">$143</text><text x="174.5" y="36.5">$150</text>
      <text x="188.5" y="34.5">$154</text><text x="202.5" y="31.5">$161</text><text x="216.5" y="29.5">$161</text><text x="230.5" y="26.5">$167</text>
    </g>
    <g font-size="2" fill="#555" text-anchor="middle">
      <text x="20.5" y="99">2003</text><text x="34.5" y="99">2004</text><text x="48.5" y="99">2005</text><text x="62.5" y="99">2006</text>
      <text x="76.5" y="99">2007</text><text x="90.5" y="99">2008</text><text x="104.5" y="99">2009</text><text x="118.5" y="99">2010</text>
      <text x="132.5" y="99">2011</text><text x="146.5" y="99">2012</text><text x="160.5" y="99">2013</text><text x="174.5" y="99">2014</text>
      <text x="188.5" y="99">2015</text><text x="202.5" y="99">2016</text><text x="216.5" y="99">2017</text><text x="230.5" y="99">2018</text>
    </g>
    <text x="235" y="104" font-size="2" fill="#555" text-anchor="end" font-style="italic">Source: National Staffing Council industry analysis</text>
  </svg>
  <div class="footer"><span class="bar"></span><span class="label">VANTORA GROUP <i></i> 01</span></div>
</section>

<section class="slide col-3 row-2" aria-label="What is our product">
  <h2 class="slide-title"><span class="kicker">What Is</span><span class="heading">Our Product?</span></h2>
  <div class="brand"><span class="dot"></span><span class="name">VANTORA GROUP</span></div>
  <div class="body">
    <p>We provide accounting and finance staffing on a contract and permanent basis.</p>
    <p class="accent" style="margin-bottom:.6px">WHO COULD USE OUR PRODUCT?</p>
    <p>Anyone who hires accounting and finance professionals on a contract or permanent basis.</p>
    <p class="accent" style="margin-bottom:.6px">WHO HIRES ACCOUNTING PROFESSIONALS?</p>
    <p>Any firm that has an accounting or finance department.</p>
    <p>So what is staffing? It is sourcing, screening and retaining professionals for a fee.</p>
    <p>We offer leased employees on contract and regular full time placement for permanent roles.</p>
    <p>Every company has business objectives to meet, and staffing is often its largest expense.</p>
    <p>People leave, firms grow and projects are won, so organizations need to add talent quickly.</p>
  </div>
  <div class="footer"><span class="bar"></span><span class="label">VANTORA GROUP <i></i> 01</span></div>
</section>

<!-- Row 3 -->
<section class="slide dark col-1 row-3" aria-label="What is full time staffing overview">
  <div class="photo" role="img" aria-label="Photo of a professional at work in an office"></div>
  <h2 class="slide-title"><span class="kicker">What Is Full</span><span class="heading" style="color:#fff">Time Staffing?</span></h2>
  <div class="brand"><span class="dot"></span><span class="name" style="color:#fff">VANTORA GROUP</span></div>
  <div class="body" style="color:#fff;top:29px">
    <p>When a staffing firm sources candidates that clients hire directly for full-time employment.</p>
    <p class="accent" style="margin-bottom:.6px">FULL TIME STAFFING:</p>
    <p>Definition: the hiring of employees on a full time basis.<br>Reason: long term need for a specific position.</p>
    <p class="accent">Contract Staffing:</p>
  </div>
  <table class="grid-table orange-head" style="position:absolute;left:10px;top:72px;width:242px">
    <tr><th>ADVANTAGES</th><th>DISADVANTAGES</th></tr>
    <tr><td>Streamline # of Employees</td><td>Lower Company Loyalty</td></tr>
    <tr><td>Hired Expertise</td><td>Cost for Specific Talent / Rate</td></tr>
    <tr><td>Reduce Training Costs</td><td>Short Term Solution</td></tr>
    <tr><td>Flexibility w/ Employees</td><td></td></tr>
    <tr><td>Overall Cost Saving (Time / $)</td><td></td></tr>
  </table>
  <div class="footer"><span class="bar"></span><span class="label">VANTORA GROUP <i></i> 01</span></div>
</section>

<section class="slide col-2 row-3" aria-label="What is full time staffing comparison">
  <h2 class="slide-title"><span class="kicker">What Is Full</span><span class="heading">Time Staffing?</span></h2>
  <div class="brand"><span class="dot"></span><span class="name">VANTORA GROUP</span></div>
  <p style="position:absolute;left:12px;top:28px;font-size:2.6px;color:var(--orange)">FULL TIME STAFFING:</p>
  <table class="grid-table navy-head" style="position:absolute;left:12px;top:36px;width:238px">
    <tr><th>ADVANTAGES</th><th>DISADVANTAGES</th></tr>
    <tr><td>Can Create Company Loyalty</td><td>Long Term Commitment</td></tr>
    <tr><td>Long Term Staffing Solutions / Team</td><td>Extensive Hiring Costs / Onboarding</td></tr>
    <tr><td>Groom in Management</td><td>Approval Process</td></tr>
    <tr><td>Cost for Specific Talent</td><td>Flexibility in Employee Resources</td></tr>
  </table>
  <div class="body" style="top:95px">
    <p class="accent">3. Project Based Objectives</p>
    <p>As organizations run more efficiently, they streamline their costs. Project based objectives help them reach short and long term goals.</p>
    <p>Project objectives are common in the accounting and finance field, where operations often run lean to reduce fixed costs.</p>
    <p>Companies meet these objectives through outsourcing and staff augmentation. Here are the differences in simple terms.</p>
  </div>
  <div class="footer"><span class="bar"></span><span class="label">VANTORA GROUP <i></i> 01</span></div>
</section>

<section class="slide col-3 row-3" aria-label="The sales cycle metrics">
  <h2 class="slide-title"><span class="kicker">The Sales</span><span class="heading">Cycle</span></h2>
  <div class="brand"><span class="dot"></span><span class="name">VANTORA GROUP</span></div>

  <div class="pie-card" style="left:16px;top:33px;width:40px;height:38px">
    <span class="cap">SUCCESSFUL PLACEMENTS<br>GOAL 85%</span>
    <svg width="30" height="26" viewBox="0 0 32 26" aria-label="Pie chart of placements">
      <ellipse cx="16" cy="15" rx="13" ry="8" fill="#c9601f"/>
      <ellipse cx="16" cy="13" rx="13" ry="8" fill="#f07a2c"/>
      <path d="M16 13 L16 5 A13 8 0 0 0 4 10 Z" fill="#2e4a7a"/>
    </svg>
  </div>
  <div class="pie-card" style="left:16px;top:104px;width:40px;height:38px">
    <span class="cap">INTERVIEW/HIRE<br>GOAL 45%</span>
    <svg width="30" height="26" viewBox="0 0 32 26" aria-label="Pie chart of interview to hire">
      <ellipse cx="16" cy="15" rx="13" ry="8" fill="#c9601f"/>
      <ellipse cx="16" cy="13" rx="13" ry="8" fill="#f07a2c"/>
      <path d="M16 13 L16 5 A13 8 0 0 1 27 17 Z" fill="#2e4a7a"/>
    </svg>
  </div>
  <div class="pie-card" style="left:203px;top:33px;width:42px;height:40px">
    <span class="cap">CANDIDATE ACCURACY<br>GOAL 75%</span>
    <svg width="30" height="26" viewBox="0 0 32 26" aria-label="Pie chart of candidate accuracy">
      <ellipse cx="16" cy="15" rx="13" ry="8" fill="#c9601f"/>
      <ellipse cx="16" cy="13" rx="13" ry="8" fill="#f07a2c"/>
      <path d="M16 13 L3 13 A13 8 0 0 1 16 5 Z" fill="#2e4a7a"/>
    </svg>
  </div>
  <div class="pie-card" style="left:203px;top:104px;width:42px;height:38px">
    <span class="cap">FILL RATES<br>GOAL 45%</span>
    <svg width="30" height="26" viewBox="0 0 32 26" aria-label="Pie chart of fill rates">
      <ellipse cx="16" cy="15" rx="13" ry="8" fill="#1f3356"/>
      <ellipse cx="16" cy="13" rx="13" ry="8" fill="#2e4a7a"/>
      <path d="M16 13 L16 5 A13 8 0 0 0 5 17 Z" fill="#f07a2c"/>
      <path d="M16 13 L5 17 A13 8 0 0 0 9 20 Z" fill="#aab0bd"/>
    </svg>
  </div>

  <div style="position:absolute;left:76px;top:31px;width:120px">
    <p style="font-size:2.4px;font-weight:700;text-align:center">SALES</p>
    <table class="stat-table">
      <tr><th>Tasks:</th><th>Production:</th><th>Goal:</th><th>% of Goal:</th></tr>
      <tr><td>Fills</td><td>190</td><td>210</td><td>91%</td></tr>
      <tr><td>Submittals</td><td>600</td><td>650</td><td>92%</td></tr>
      <tr><td>Interviews</td><td>332</td><td>328</td><td class="hl">95%</td></tr>
      <tr><td>Reqs</td><td>341</td><td>315</td><td class="hl">108%</td></tr>
      <tr><td>DMC</td><td>364</td><td>492</td><td class="hl">83%</td></tr>
      <tr><td>Total Meetings</td><td>1,120</td><td>2,562</td><td class="hl">46%</td></tr>
      <tr><td>Total Contacts</td><td>28,359</td><td>20,177</td><td class="hl">141%</td></tr>
      <tr><td>New Contacts</td><td>1,369</td><td>2,868</td><td class="hl">48%</td></tr>
    </table>
    <p style="font-size:2.4px;font-weight:700;margin-top:2px">% AVG ACTIVITY: <span style="margin-left:40px">85%</span></p>
    <p style="font-size:2.4px;font-weight:700;text-align:center;margin-top:4px">RECRUITING</p>
    <table class="stat-table">
      <tr><th>Tasks:</th><th>Production:</th><th>Goal:</th><th>% of Goal:</th></tr>
      <tr><td>Fills</td><td>146</td><td>215</td><td>91%</td></tr>
      <tr><td>Interviews</td><td>335</td><td>345</td><td class="hl">92%</td></tr>
      <tr><td>Submittals</td><td>369</td><td>362</td><td class="hl">91%</td></tr>
      <tr><td>NI</td><td>5,305</td><td>4,754</td><td class="hl">86%</td></tr>
      <tr><td>Matches</td><td>17,771</td><td>11,964</td><td class="hl">86%</td></tr>
      <tr><td>Contacts</td><td>12,659</td><td>10,224</td><td class="hl">101%</td></tr>
      <tr><td>CN Network</td><td>13,783</td><td>21,453</td><td class="hl">64%</td></tr>
    </table>
    <p style="font-size:2.4px;font-weight:700;margin-top:2px">% AVG ACTIVITY: <span style="margin-left:40px">93%</span></p>
  </div>
  <div class="footer"><span class="bar"></span><span class="label">VANTORA GROUP <i></i> 01</span></div>
</section>

<!-- Row 4 -->
<section class="slide col-1 row-4" aria-label="The sales cycle phases">
  <h2 class="slide-title"><span class="kicker">The Sales</span><span class="heading">Cycle</span></h2>
  <div class="brand"><span class="dot"></span><span class="name">VANTORA GROUP</span></div>
  <div class="body" style="right:135px">
    <p>What is territory knowledge and why does it matter? We begin with the end goal in mind: to make placements. Every plan needs a clear path to success.</p>
    <p>Think of a territory as a puzzle. Spread the pieces on a table, group them by shape and color, build the border, then fill in each section one group at a time until the picture is complete.</p>
  </div>
  <div class="body" style="top:108px">
    <p>Sounds easy, right? A territory has moving parts, from new offices to changing staff, so understanding it should be the base of your approach.</p>
    <p style="margin:0"><span class="accent" style="font-weight:400">Phase 1:</span> Prospecting / Market Research<br><span class="accent" style="font-weight:400">Phase 2:</span> Account Penetration / Company Research<br><span class="accent" style="font-weight:400">Phase 3:</span> Obtaining Business / Service Delivery<br><span class="accent" style="font-weight:400">Phase 4:</span> Account Retention</p>
  </div>
  <svg style="position:absolute;left:130px;top:28px" width="124" height="78" viewBox="0 0 124 78" aria-label="Four phase sales cycle diagram">
    <text x="62" y="7" font-size="4.4" text-anchor="middle" fill="#222">Sales Cycle</text>
    <g font-size="1.8" text-anchor="middle" fill="#333">
      <rect x="48" y="14" width="28" height="10" fill="#f5d20a" stroke="#b89a00" stroke-width=".4"/><text x="62" y="18.5">Phase 1</text><text x="62" y="21.5">PROSPECTING</text>
      <rect x="92" y="33" width="28" height="10" fill="#d9a21a" stroke="#9b7410" stroke-width=".4"/><text x="106" y="37.5">Phase 2</text><text x="106" y="40.5">ACCOUNT PENETRATION</text>
      <rect x="48" y="55" width="28" height="10" fill="#e08a1e" stroke="#a2610e" stroke-width=".4"/><text x="62" y="59.5">Phase 3</text><text x="62" y="62.5">OBTAINING BUSINESS</text>
      <rect x="4" y="33" width="28" height="10" fill="#c8321e" stroke="#8d1f12" stroke-width=".4"/><text x="18" y="37.5" fill="#fff">Phase 4</text><text x="18" y="40.5" fill="#fff">ACCOUNT RETENTION</text>
    </g>
    <g fill="none" stroke="#4caf3a" stroke-width="2.6" stroke-linecap="round">
      <path d="M80 18 Q98 20 102 29"/><path d="M102 47 Q98 58 80 60"/><path d="M44 60 Q26 58 22 47"/><path d="M22 29 Q26 20 44 18"/>
    </g>
    <g fill="#4caf3a">
      <path d="M99 28 L106 28 L102.5 33 Z"/><path d="M81 57 L81 63 L76 60 Z"/><path d="M19 48 L26 48 L22.5 43 Z"/><path d="M43 15 L43 21 L48 18 Z"/>
    </g>
  </svg>
  <div class="footer"><span class="bar"></span><span class="label">VANTORA GROUP <i></i> 01</span></div>
</section>

<section class="slide col-2 row-4" aria-label="Profits and losses chart">
  <h2 class="slide-title"><span class="kicker">Sales Training</span><span class="heading">Introduction</span></h2>
  <div class="brand"><span class="dot"></span><span class="name">VANTORA GROUP</span></div>
  <svg style="position:absolute;left:0;top:22px" width="262" height="136" viewBox="0 0 262 136" aria-label="Profits and losses by month, January to June">
    <line x1="18" y1="68" x2="196" y2="68" stroke="#2b3446" stroke-width=".8"/>
    <line x1="196" y1="68" x2="196" y2="61" stroke="#2b3446" stroke-width=".8"/>
    <line x1="196" y1="61" x2="196" y2="68" stroke="#f07a2c" stroke-width=".8"/>
    <line x1="196" y1="62" x2="242" y2="62" stroke="#f07a2c" stroke-width=".8"/>
    <circle cx="18" cy="68" r="3.4" fill="#fff" stroke="#2b3446" stroke-width=".8"/><path d="M16.2 68 H19.8 M18 66.2 V69.8" stroke="#2b3446" stroke-width=".7"/>
    <circle cx="244" cy="62" r="3.4" fill="#f07a2c"/><path d="M242.2 62 H245.8" stroke="#fff" stroke-width=".7"/>
    <g fill="#2b3446">
      <path d="M27 64 V58 a5 5 0 0 1 10 0 V64 Z"/>
      <path d="M44 64 V52 a5 5 0 0 1 10 0 V64 Z"/>
      <path d="M61 64 V45 a5 5 0 0 1 10 0 V64 Z"/>
      <path d="M78 64 V37 a5 5 0 0 1 10 0 V64 Z"/>
      <path d="M95 64 V28 a5 5 0 0 1 10 0 V64 Z"/>
    </g>
    <g fill="#fff"><circle cx="32" cy="59" r="1.6"/><circle cx="49" cy="56" r="1.6"/><circle cx="66" cy="52" r="1.6"/><circle cx="83" cy="47" r="1.6"/><circle cx="100" cy="41" r="1.6"/></g>
    <g font-size="3.6" fill="#2b3446" text-anchor="middle" font-weight="600">
      <text x="32" y="51">10%</text><text x="49" y="45">20%</text><text x="66" y="38">30%</text><text x="83" y="30">40%</text><text x="100" y="21">50%</text>
    </g>
    <rect x="52" y="72" width="22" height="4" rx="2" fill="#2b3446"/><text x="63" y="74.9" font-size="2" fill="#fff" text-anchor="middle">JANUARY – JUNE</text>
    <text x="63" y="108" font-size="7" fill="#2b3446" text-anchor="middle" font-weight="600">Profits</text>
    <text x="63" y="113" font-size="2" fill="#999" text-anchor="middle">Lorem ipsum dolor sit amet, consectetuer</text>
    <text x="63" y="116" font-size="2" fill="#999" text-anchor="middle">adipiscing elit, sed diam nonummy nibh</text>

    <text x="153" y="28" font-size="7" fill="#f07a2c" text-anchor="middle" font-weight="600" font-style="italic">Losses</text>
    <text x="153" y="33" font-size="2" fill="#999" text-anchor="middle">Lorem ipsum dolor sit amet, consectetuer</text>
    <text x="153" y="36" font-size="2" fill="#999" text-anchor="middle">adipiscing elit, sed diam nonummy nibh</text>
    <rect x="142" y="54" width="22" height="4" rx="2" fill="#f07a2c"/><text x="153" y="56.9" font-size="2" fill="#fff" text-anchor="middle">JANUARY – JUNE</text>
    <g fill="#f07a2c">
      <path d="M130 66 V72 a5 5 0 0 0 10 0 V66 Z"/>
      <path d="M147 66 V78 a5 5 0 0 0 10 0 V66 Z"/>
      <path d="M164 66 V85 a5 5 0 0 0 10 0 V66 Z"/>
      <path d="M181 66 V93 a5 5 0 0 0 10 0 V66 Z"/>
      <path d="M198 66 V102 a5 5 0 0 0 10 0 V66 Z"/>
    </g>
    <g fill="#fff"><circle cx="135" cy="71" r="1.6"/><circle cx="152" cy="76" r="1.6"/><circle cx="169" cy="83" r="1.6"/><circle cx="186" cy="91" r="1.6"/><circle cx="203" cy="100" r="1.6"/></g>
    <g font-size="3.6" fill="#2b3446" text-anchor="middle" font-weight="600">
      <text x="135" y="82">10%</text><text x="152" y="88">20%</text><text x="169" y="95">30%</text><text x="186" y="103">40%</text><text x="203" y="112">50%</text>
    </g>
  </svg>
  <div class="footer"><span class="bar"></span><span class="label">VANTORA GROUP <i></i> 01</span></div>
</section>

<section class="slide dark col-3 row-4" aria-label="Thank you slide">
  <div class="photo" role="img" aria-label="Photo of a professional working at a laptop in an office"></div>
  <div class="hero-tab" style="width:104px;height:36px;left:14px;"><span class="dot"></span><span class="name">VANTORA GROUP</span></div>
  <h2 class="hero-title" style="left:14px;top:46px;font-size:9.6px;line-height:10.5px;">Powering<br><em>Progression</em><br>With People
    <span class="hero-sub" style="display:block">Recruitment solutions for an evolving marketplace.</span></h2>
  <p class="thanks" style="left:14px;top:105px;">THANK <em>YOU!</em></p>
  <span class="url" style="left:14px;top:155px;">www.vantoragroup.com</span>
</section>

</body>
</html>
```